Keystone Physical Therapy needs a New website look and update!

New updated look. Most people do not know they can go directly to a physical therapist for care. Cost effective and specialized. Getting back to your life and activity is what we do. What we treat. Your first cost effective provider for pain" for example. We treat children to seniors. Theme should be warm, caring, individualized, respect your time, and cost -effective. Mobile phone ready. Encourage taking action to call and schedule to get back to life, sports, activity.
Add link to send appointment request or contact us now
Add link ( code) for patients to fill out intake form or appointment request. I want to add testimonials for other therapists.
***My current website is "brellowkeypt.net"

```html
<!DOCTYPE html>
<html lang="en">
<head>
<meta charset="utf-8">
<title>Keystone Physical Therapy</title>
<link href="https://fonts.googleapis.com/css2?family=Questrial&family=Open+Sans:wght@400;600;700&display=swap" rel="stylesheet">
<style>
:root{
  --lime:#8cc31f;
  --lime-bright:#9ad326;
  --teal:#117d8c;
  --navy:#121c27;
  --navy-deep:#0b131c;
  --ink:#3b4752;
  --muted:#6f7a84;
  --white:#ffffff;
  --field:#eef0f2;
}
*{margin:0;padding:0;box-sizing:border-box}
html,body{width:1200px;height:4317px;overflow:hidden}
body{position:relative;font-family:"Open Sans",Arial,sans-serif;color:var(--ink);background:var(--white)}
.abs{position:absolute}
.heading{font-family:"Questrial",Arial,sans-serif;font-weight:400}
.accent{color:var(--lime)}
.btn{display:inline-block;background:var(--lime);color:var(--white);font-family:"Open Sans",Arial,sans-serif;font-weight:700;font-size:15px;text-transform:uppercase;border-radius:30px;text-align:center;text-decoration:none}
.btn-ghost{display:inline-block;border:2px solid var(--white);color:var(--white);font-weight:700;font-size:14px;border-radius:30px;text-align:center;text-transform:uppercase}

/* nav */
.topnav{left:0;top:0;width:1200px;height:63px;background:var(--navy-deep);display:flex;align-items:center;padding:0 78px}
.topnav ul{list-style:none;display:flex;gap:34px}
.topnav li{color:var(--white);font-size:14px;font-weight:600;display:flex;align-items:center;gap:9px}
.topnav li::before{content:"";width:7px;height:7px;border-radius:50%;background:var(--white)}
.topnav li.active{color:var(--lime)}
.topnav li.active::before{background:var(--lime)}
.topnav .phone{margin-left:auto;color:var(--lime);font-weight:700;font-size:16px;display:flex;align-items:center;gap:9px}

/* hero */
.hero{left:0;top:63px;width:1200px;height:613px;background:radial-gradient(ellipse at 50% 45%,#4e6f8a 0%,#1d3447 45%,#0a141e 100%)}
.brand{left:0;top:112px;width:1200px;display:flex;justify-content:center;align-items:center;gap:16px}
.brand .dot{width:58px;height:58px;border-radius:50%;background:var(--lime)}
.brand .name{font-family:"Questrial",Arial,sans-serif;font-size:48px;color:var(--lime)}
.hero-title{left:120px;top:327px;width:960px;text-align:center;color:var(--white);font-size:40px;line-height:48px;font-weight:700;font-family:"Open Sans",Arial,sans-serif}

/* welcome */
.welcome-bg{left:0;top:676px;width:1200px;height:450px;background:var(--lime)}
.welcome-cut{left:0;top:676px;width:1200px;height:450px}
.welcome-title{left:78px;top:745px;font-size:40px;color:var(--teal)}
.welcome-title span{color:var(--white)}
.welcome-text{left:78px;top:810px;width:800px;color:var(--white);font-size:14px;line-height:22px}
.welcome-text p+p{margin-top:12px}
.round-photo{border-radius:50%;border:6px solid var(--white);overflow:hidden}

/* services */
.section-title{width:1200px;left:0;text-align:center;font-size:44px;color:var(--teal)}
.section-sub{width:1200px;left:0;text-align:center;font-size:15px;color:var(--muted)}
.service{width:248px;height:225px}
.service .img{height:170px}
.service .label{height:55px;background:var(--lime);color:var(--white);font-size:17px;display:flex;align-items:center;justify-content:center}

/* provider */
.provider-band{left:0;top:1820px;width:1200px;height:690px}
.provider{width:270px;text-align:center;color:var(--white)}
.provider .face{width:207px;height:207px;margin:0 auto;border-radius:50%;border:6px solid var(--white);background:linear-gradient(160deg,#c9a58a,#7d5c48)}
.provider h3{margin-top:26px;font-size:19px;font-weight:700}
.provider p{margin-top:10px;font-size:13px;line-height:20px;color:#e9f6f0}

/* testimonials */
.reviews{left:0;top:2505px;width:1200px;height:560px;background:radial-gradient(ellipse at 50% 40%,#1f3140,#0a121a 80%)}
.arrow{width:44px;height:44px;border-radius:50%;border:2px solid #6c7884}
.quote{left:150px;top:2800px;width:900px;text-align:center;color:#cfd6dc;font-size:14px;line-height:24px}
.client{left:0;top:2896px;width:1200px;text-align:center;color:var(--lime);font-size:14px;font-weight:700}

/* form */
.field{background:var(--field);border:1px solid #dde1e5;color:#9aa3ab;font-size:13px;padding:10px 12px}

/* store */
.store-text{left:430px;width:692px;text-align:right;color:var(--white)}

/* footer */
.footer{left:0;top:3842px;width:1200px;height:432px;background:linear-gradient(180deg,#16222d,#0f1821)}
.footer h4{font-size:18px;font-weight:400;color:var(--lime);text-transform:uppercase;font-family:"Questrial",Arial,sans-serif}
.footer p,.footer li{color:#c9d0d6;font-size:14px;line-height:24px}
.foot-links{list-style:none;display:flex;gap:24px}
.contact-row{display:flex;align-items:center;gap:16px;color:#c9d0d6;font-size:14px;line-height:20px}
.copyright{left:0;top:4274px;width:1200px;height:43px;background:var(--navy-deep);color:#9aa3ab;font-size:13px;text-align:center;line-height:43px}
.copyright span{color:var(--lime)}
</style>
</head>
<body>

<nav class="abs topnav">
  <ul>
    <li class="active">HOME</li><li>ABOUT US</li><li>SERVICES</li><li>FAQ</li><li>FORMS</li><li>INSURANCE</li><li>CONTACT US</li>
  </ul>
  <div class="phone">
    <svg width="16" height="16" viewBox="0 0 24 24"><path fill="#8cc31f" d="M6.6 10.8a15 15 0 0 0 6.6 6.6l2.2-2.2c.3-.3.7-.4 1-.2 1.1.4 2.3.6 3.6.6.6 0 1 .4 1 1V20c0 .6-.4 1-1 1A17 17 0 0 1 3 4c0-.6.4-1 1-1h3.5c.6 0 1 .4 1 1 0 1.3.2 2.5.6 3.6.1.3 0 .7-.2 1z"/></svg>
    555-214-0387
  </div>
</nav>

<section class="hero abs" role="img" aria-label="Swimmer diving through splashing water on a dark background"></section>
<div class="abs brand"><span class="dot"></span><span class="name">Keystone Physical Therapy</span></div>
<h1 class="abs hero-title">Our practice is to restoration, wellness and quality of life providing compassionate, skilled care to clients of all <span class="accent">AGES.</span></h1>
<div class="abs" style="left:485px;top:503px"><a class="btn" style="width:230px;height:52px;line-height:52px">Book Appointment</a></div>

<section class="welcome">
  <div class="abs welcome-bg"></div>
  <svg class="abs welcome-cut" width="1200" height="450" viewBox="0 0 1200 450"><polygon points="0,430 1200,270 1200,450 0,450" fill="#ffffff"/></svg>
  <h2 class="abs heading welcome-title">Welcome To <span>Keystone Physical Therapy</span></h2>
  <div class="abs welcome-text">
    <p>Welcome to Keystone Physical Therapy, southeast Denver's choice for healing and rehabilitation. Our therapist owned practice is committed to restoration, wellness and quality of life providing compassionate, skilled care to clients of all ages.</p>
    <p>Keystone Physical Therapy treats a wide range of injuries and conditions, whether you're recovering from surgery, returning to athletics or enhancing sports performance. Partnering with you to achieve and maintain a healthy, vigorous lifestyle, our therapists deliver exceptional.</p>
  </div>
  <a class="btn-ghost" style="position:absolute;left:78px;top:987px;width:168px;height:48px;line-height:44px">Know More</a>
  <div class="abs round-photo" style="left:920px;top:771px;width:202px;height:202px;background:linear-gradient(160deg,#dfe6ee,#3b4f7a)" role="img" aria-label="Figure skater in a blue dress posing on the ice"></div>
</section>

<h2 class="abs heading section-title" style="top:1132px">Our <span class="accent">Services</span></h2>
<div class="abs section-sub" style="top:1193px">What We Do</div>

<div class="abs service" style="left:78px;top:1252px"><div class="img" style="background:linear-gradient(135deg,#c79b7c,#5a3c2c)" role="img" aria-label="Dry needling treatment on a patient's back"></div><div class="label">Dry Needling</div></div>
<div class="abs service" style="left:343px;top:1252px"><div class="img" style="background:linear-gradient(135deg,#e4d9cc,#8a7866)" role="img" aria-label="Group pilates class in a studio"></div><div class="label">Pilates</div></div>
<div class="abs service" style="left:608px;top:1252px"><div class="img" style="background:linear-gradient(135deg,#7a5a52,#2b2225)" role="img" aria-label="Runner on a treadmill during gait analysis"></div><div class="label">Running Gait Analysis</div></div>
<div class="abs service" style="left:873px;top:1252px"><div class="img" style="background:linear-gradient(135deg,#d9c3b2,#6c6470)" role="img" aria-label="Laser therapy applied to a patient's shoulder"></div><div class="label">Laser &amp; Infrared Therapy</div></div>

<div class="abs service" style="left:78px;top:1488px"><div class="img" style="background:linear-gradient(135deg,#eef0f3,#8b8f97)" role="img" aria-label="Therapist giving a massage to a seated patient"></div><div class="label">Massage Therapy</div></div>
<div class="abs service" style="left:343px;top:1488px"><div class="img" style="background:linear-gradient(135deg,#6b6f77,#1d1f24)" role="img" aria-label="Athlete doing a plank in functional training"></div><div class="label">Functional Sport Training</div></div>
<div class="abs service" style="left:608px;top:1488px"><div class="img" style="background:linear-gradient(135deg,#5c6a7c,#22262f)" role="img" aria-label="Alignment training with exercise balls in a gym"></div><div class="label">Alignment Training</div></div>
<div class="abs service" style="left:873px;top:1488px"><div class="img" style="background:linear-gradient(135deg,#e6d3b0,#9a7a56)" role="img" aria-label="Core stabilization exercise on a stability ball"></div><div class="label">Core Stabilization &amp; Pilate</div></div>

<div class="abs" style="left:517px;top:1738px"><a class="btn" style="width:166px;height:52px;line-height:52px">Know More</a></div>

<svg class="abs provider-band" width="1200" height="690" viewBox="0 0 1200 690">
  <defs><linearGradient id="provGrad" x1="0" y1="0" x2="1" y2="0.3"><stop offset="0" stop-color="#8cc31f"/><stop offset="1" stop-color="#127b8c"/></linearGradient></defs>
  <polygon points="0,160 1200,0 1200,690 0,690" fill="url(#provGrad)"/>
</svg>
<div class="abs round-photo" style="left:80px;top:1776px;width:280px;height:280px;background:linear-gradient(160deg,#eef3f6,#4a7fb0)" role="img" aria-label="Senior woman exercising on a blue stability ball"></div>
<h2 class="abs heading" style="left:477px;top:1975px;font-size:44px;color:var(--teal)">Our <span style="color:var(--lime-bright)">Provider</span></h2>

<div class="abs provider" style="left:70px;top:2078px"><div class="face" role="img" aria-label="Portrait of the practice owner"></div><h3>Dana Whitfield, PT, Owner</h3><p>Physical therapist Dana Whitfield opened Keystone PT in 2005 to provide personalized orthopedics and sports medicine.</p></div>
<div class="abs provider" style="left:337px;top:2078px"><div class="face" role="img" aria-label="Portrait of a physical therapist"></div><h3>Carly Brennan, PT, MS</h3><p>Carly was born, raised, and educated in western Montana. Her exposure and interest in physical therapy began at an early.</p></div>
<div class="abs provider" style="left:596px;top:2078px"><div class="face" role="img" aria-label="Portrait of a physical therapist"></div><h3>Renee Castillo, DPT, SCS</h3><p>Renee Castillo, DPT, SCS received her BS in Exercise Science at Westbrook University. She received her Doctorate.</p></div>
<div class="abs provider" style="left:861px;top:2078px"><div class="face" role="img" aria-label="Portrait of a physical therapist"></div><h3>Jenna Morrow, MPT</h3><p>Jenna was born and raised in St. Louis, MO. She grew up playing sports, including softball, volleyball and soccer, but chose.</p></div>

<section class="abs reviews" role="img" aria-label="Dark textured background with a faint athlete silhouette"></section>
<h2 class="abs heading section-title" style="top:2575px;font-size:44px;color:var(--teal)">What Our <span class="accent">Client Say</span></h2>
<div class="abs round-photo" style="left:545px;top:2660px;width:110px;height:110px;border-width:4px;background:linear-gradient(160deg,#f1ece6,#b39a86)" role="img" aria-label="Client portrait"></div>
<div class="abs arrow" style="left:78px;top:2721px"><svg width="40" height="40" viewBox="0 0 40 40"><path d="M23 12 15 20l8 8" stroke="#9aa5b0" stroke-width="2.5" fill="none"/></svg></div>
<div class="abs arrow" style="left:1078px;top:2721px"><svg width="40" height="40" viewBox="0 0 40 40"><path d="M17 12l8 8-8 8" stroke="#9aa5b0" stroke-width="2.5" fill="none"/></svg></div>
<p class="abs quote">" Lorem Ipsum is simply dummy text of the printing and typesetting industry. Lorem Ipsum has been the industry's standard dummy text ever since the 1500s, when an unknown printer took a galley of type and scrambled it to make a type specimen book, and typesetting industry. Lorem Ipsum has been the industry's "</p>
<div class="abs client">- CLIENT NAME</div>

<div class="abs round-photo" style="left:849px;top:2878px;width:273px;height:273px;background:linear-gradient(160deg,#f3f5f7,#2d5ea8)" role="img" aria-label="Soccer player kicking a ball"></div>

<h2 class="abs heading section-title" style="top:3115px;font-size:46px;color:var(--teal)">Request An <span class="accent">Appointment</span></h2>
<div class="abs field" style="left:201px;top:3203px;width:312px;height:52px">Name*</div>
<div class="abs field" style="left:527px;top:3203px;width:470px;height:52px">Email*</div>
<div class="abs field" style="left:201px;top:3266px;width:312px;height:52px">Phone*</div>
<div class="abs field" style="left:527px;top:3266px;width:470px;height:110px">Description*</div>
<div class="abs field" style="left:201px;top:3325px;width:312px;height:52px">Services*</div>
<div class="abs" style="left:517px;top:3390px"><a class="btn" style="width:166px;height:52px;line-height:52px">Submit</a></div>

<svg class="abs" style="left:0;top:3440px" width="1200" height="402" viewBox="0 0 1200 402"><polygon points="0,130 1200,20 1200,402 0,402" fill="#8cc31f"/></svg>
<div class="abs round-photo" style="left:78px;top:3448px;width:276px;height:276px;background:linear-gradient(160deg,#f4f6f2,#5f7d3c)" role="img" aria-label="Sports gear: jersey, hockey sticks, soccer ball and racket"></div>
<h2 class="abs heading store-text" style="top:3578px;font-size:44px;color:var(--teal)">Our <span style="color:var(--white)">Online</span> Pt Store</h2>
<div class="abs store-text" style="top:3650px;font-size:15px">http://www.kptgearshop.biz#oid=2051_4</div>
<p class="abs store-text" style="top:3690px;font-size:13px;line-height:22px;color:#f3f9e8">Please click on the above link to reach Online PT Store! You may order Exercise equipment such as Balls, Tubing, Foam Rollers. Orthopedic supports and braces for knees, ankles, etc. Pain control: cooling gel, therapy tape, and much, much More!</p>

<footer class="abs footer">
  <h4 class="abs" style="left:78px;top:60px">About Us</h4>
  <p class="abs" style="left:78px;top:105px;width:470px">Welcome to Keystone Physical Therapy, southeast Denver's choice for healing and rehabilitation. Our therapist owned practice is committed to restoration, wellness and quality of life providing compassionate, skilled care to clients of all ages.</p>
  <ul class="abs foot-links" style="left:78px;top:305px"><li>Home</li><li>About Us</li><li>Services</li><li>Faq</li><li>Forms</li><li>Insurance</li><li>Contact Us</li></ul>

  <h4 class="abs" style="left:639px;top:60px">We Are Everywhere</h4>
  <div class="abs contact-row" style="left:639px;top:100px">
    <svg width="18" height="18" viewBox="0 0 24 24"><path fill="#8cc31f" d="M6.6 10.8a15 15 0 0 0 6.6 6.6l2.2-2.2c.3-.3.7-.4 1-.2 1.1.4 2.3.6 3.6.6.6 0 1 .4 1 1V20c0 .6-.4 1-1 1A17 17 0 0 1 3 4c0-.6.4-1 1-1h3.5c.6 0 1 .4 1 1 0 1.3.2 2.5.6 3.6.1.3 0 .7-.2 1z"/></svg>
    555-214-0387</div>
  <div class="abs contact-row" style="left:639px;top:142px">
    <svg width="18" height="22" viewBox="0 0 24 24"><path fill="#8cc31f" d="M12 2a7 7 0 0 0-7 7c0 5.2 7 13 7 13s7-7.8 7-13a7 7 0 0 0-7-7zm0 9.5A2.5 2.5 0 1 1 12 6.5a2.5 2.5 0 0 1 0 5z"/></svg>
    <span>Mainstreet Location Clinic<br>4870 Harlow Avenue, Suite 112 Ridgeford, CO 80877</span></div>
  <div class="abs contact-row" style="left:639px;top:200px">
    <svg width="18" height="18" viewBox="0 0 24 24"><path fill="#8cc31f" d="M6.6 10.8a15 15 0 0 0 6.6 6.6l2.2-2.2c.3-.3.7-.4 1-.2 1.1.4 2.3.6 3.6.6.6 0 1 .4 1 1V20c0 .6-.4 1-1 1A17 17 0 0 1 3 4c0-.6.4-1 1-1h3.5c.6 0 1 .4 1 1 0 1.3.2 2.5.6 3.6.1.3 0 .7-.2 1z"/></svg>
    555-214-0392</div>
  <h4 class="abs" style="left:639px;top:248px">Newsletter Signup</h4>
  <div class="abs" style="left:639px;top:294px;width:469px;height:44px;border:1px solid #5a6672;display:flex;align-items:center;justify-content:space-between;padding:0 16px;color:#c9d0d6;font-size:13px">
    Enter Email Id here
    <svg width="20" height="16" viewBox="0 0 20 16"><rect x="1" y="2" width="18" height="12" fill="#8cc31f"/><path d="M1 2l9 7 9-7" stroke="#121c27" stroke-width="1.5" fill="none"/></svg>
  </div>
</footer>
<div class="abs copyright">© <span>Keystone Physical Therapy</span> - 2017. All Rights Reserved</div>

</body>
</html>
```